Boutique Salon Brand Refresh needs color palette, font, templates.

Tovel Hair Design is an established hair salon celebrating 10 years in business. We are currently evolving our brand to better reflect who we are today, the clients we serve, and the direction we want to take our business moving forward.
Our goal is to position Tovel as a refined, modern boutique salon created specifically for “The Tovel Woman.”
In the past, much of our branding and marketing focused on us—our salon, our space, our services, and our team. Going forward, we want to shift that focus to her: who she is, what she values, how she wants to look and feel, and how Tovel fits into her life.
We want our brand to communicate expertise and quality without feeling overly luxurious, trendy, intimidating, or impersonal. It should feel polished, sophisticated, warm, approachable, and timeless—a boutique experience designed for women who value beautiful, healthy hair and trusted professional guidance.
As part of this rebrand, we are looking to establish a cohesive visual identity that can be carried consistently across our website, social media, email marketing, print materials, signage, and other client touchpoints.

*** For THIS PROJECT, we are SPECIFICALLY LOOKING for:
- A cohesive brand color palette
- 2–3 complementary fonts for consistent use across our marketing
- 4–5 customizable social media templates that can be used across Instagram and Facebook
A visual direction that feels distinctive to Tovel and speaks directly to The Tovel Woman.
The following information provides more detail about The Tovel Woman, our positioning, brand personality, values, and the overall direction we envision for the next chapter of Tovel Hair Design.
Tovel Hair Design
Mendham, NJ USA
tovelhairstudio-example.com

--PRIMARY AUDIENCE
The Tovel woman values quality, consistency, and professional guidance.
She wants to look polished and current without appearing overdone or overly trendy.
She may be managing grey hair, changing texture, thinning, dryness, fading color, or a style that no longer reflects who she is. She wants an expert who understands these concerns and can create a realistic plan.
She is willing to invest in professional services and products when she understands their value.
She does not want to experiment with her appearance.
She wants to feel confident in the person caring for her hair.
Women approximately 45 to 65 years old living in Mendham, Morris County, and surrounding communities.

--COLOR PALETTE
The overall appearance should feel calm, spacious, editorial, and cohesive. The entire visual system should feel more like a refined boutique hotel, skincare brand, or luxury lifestyle publication than a traditional salon advertisement.
When choosing the palette, we want the colors to invoke these feelings.
Represents:
Expertise
Confidence
Timelessness
Professionalism
Calm
Warmth
Cleanliness
Soft luxury
Natural beauty
Warmth
Balance
Subtle sophistication
Consistency

--TYPOGRAPHY
The typography system should feel refined, modern, readable, and timeless.
Recommended usage for each font, size, spacing, etc.

----TEMPLATE IDEAS
**EDUCATIONAL POST
Frequently asked questions
Healthy-hair advice
Healthy Hair Tip
Grey Coverage FAQ
Grey Blending FAQ
Product education
Single-tip graphic
**REVIEWS
Google reviews
Finest of Brookvale recognition/Community awards
Long-term guest relationships
Guest testimonials/satisfaction stories
Referral stories
**ADS
**SALON UPDATES/INFO
Holiday hours
Policy reminder
New guest guide
Consultation invitation
Service spotlight
Seasonal guidance
**ABOUT TOVEL
Who we are
What to expect from us
What we can provide
Our expertise
**HIGHLIGHT ICON
Questions
Testimonial
Product
Reminders

TEMPLATE RULES
Use the color palette
Use only the font system
Maintain generous spacing
Limit text
Use consistent margins
Keep calls to action simple
Avoid crowded layouts
Use photography intentionally
Keep every template recognizably Tovel

Target Market(s)

Women approximately 45 to 65 years old living in Mendham, Morris County, and surrounding communities. She values quality, consistency, and professional guidance. She wants to look polished and current without appearing overdone or overly trendy. She is willing to invest in professional services and products when she understands their value.

Industry/Entity Type

Hair Salon

Font styles to use
Serif
Sans Serif
Script

Requirements
Must have
• We are looking to establish a cohesive visual identity that can be carried consistently across platforms. It should communicate expertise and quality without feeling overly fluffy, trendy, intimidating, or impersonal. I would like to see multiple template ideas. Example- one template for education post, one template for reviews, one for salon information/updates. etc. My main goal here is to simplify social media posts by having designated templates for each post category. WE WILL BE KEEPING OUR ORGINAL LOGO- SO COLOR PALETTE MUST REFLECT THAT.
Nice to have
• Color palette and font sets that reflect the brand. **cohesive visual identity**
Should not have
• Nothing flashy, busy, overly trendy.

```html
<!DOCTYPE html>
<html lang="en">
<head>
<meta charset="utf-8">
<title>Tovel Hair Design — Brand Identity Board</title>
<link rel="stylesheet" href="https://fonts.googleapis.com/css2?family=Alex+Brush&family=Montserrat:wght@400;500;700&family=Playfair+Display:wght@400;500;700&display=swap">
<style>
  :root {
    --brand-red: #b71f31;
    --linen: #ddd5cb;
    --taupe: #bfb2a2;
    --blush: #efcbc3;
    --sage: #9fa896;
    --ink: #050809;
    --paper: #ffffff;
    --rule-grey: #a7a7a7;
    --serif: "Playfair Display", Georgia, serif;
    --sans: "Montserrat", Arial, sans-serif;
    --script: "Alex Brush", cursive;
  }
  * { box-sizing: border-box; margin: 0; padding: 0; }
  html, body { width: 877px; height: 1200px; overflow: hidden; background: var(--paper); }
  .board { position: relative; width: 877px; height: 1200px; background: var(--paper); color: var(--ink); font-family: var(--sans); }
  .abs { position: absolute; }

  /* Section headings */
  .section-title { position: absolute; font: 400 16.5px/1 var(--sans); letter-spacing: 0.8px; color: var(--ink); }
  .section-rule { position: absolute; height: 1.5px; width: 148px; background: var(--rule-grey); }

  /* Primary wordmark */
  .wordmark { position: absolute; text-align: left; color: var(--ink); font-family: var(--serif); font-weight: 400; }
  .wordmark .name { display: block; font-size: 96px; line-height: 1; letter-spacing: -1px; }
  .wordmark .descriptor { display: block; font-size: 17px; letter-spacing: 0.5px; text-transform: uppercase; margin-top: 6px; }

  /* Logo tiles */
  .logo-tile { position: absolute; top: 72px; width: 194px; height: 194px; border-radius: 21px; display: flex; flex-direction: column; align-items: center; justify-content: center; color: var(--paper); font-family: var(--serif); font-weight: 400; }
  .logo-tile.on-ink { left: 439px; background: var(--ink); }
  .logo-tile.on-red { left: 646px; background: var(--brand-red); }
  .logo-tile .name { font-size: 56px; line-height: 1; }
  .logo-tile .descriptor { font-size: 10px; letter-spacing: 0.4px; text-transform: uppercase; margin-top: 6px; }

  /* Palette */
  .swatch { position: absolute; width: 66px; height: 66px; border-radius: 6px; }
  .swatch.red { background: var(--brand-red); }
  .swatch.linen { background: var(--linen); }
  .swatch.taupe { background: var(--taupe); }
  .swatch.blush { background: var(--blush); }
  .swatch.sage { background: var(--sage); }
  .swatch.ink { background: var(--ink); }

  /* Typography specimens */
  .specimen-glyph { position: absolute; left: 436px; line-height: 1; color: var(--ink); }
  .specimen-glyph.serif { top: 348px; font: 400 112px/1 var(--serif); }
  .specimen-glyph.sans { top: 470px; font: 400 104px/1 var(--sans); }
  .specimen-glyph.script { top: 590px; font: 400 92px/1 var(--script); }
  .spec-label { position: absolute; left: 586px; font: 700 6.8px/1 var(--sans); letter-spacing: 0.3px; text-transform: uppercase; }
  .spec-name { position: absolute; left: 586px; color: var(--ink); line-height: 1; }
  .spec-weights { position: absolute; left: 586px; font-size: 10.5px; line-height: 1; }
  .spec-sample { position: absolute; left: 586px; width: 210px; font-size: 5.3px; line-height: 7.2px; }
  .serif-set { font-family: var(--serif); }
  .sans-set { font-family: var(--sans); }
  .script-set { font-family: var(--script); }

  /* Social post templates */
  .post { position: absolute; width: 194px; height: 194px; overflow: hidden; box-shadow: 2px 3px 6px rgba(0,0,0,0.18); }
  .post.red { background: var(--brand-red); }
  .post.sage { background: var(--sage); }
  .post.blush { background: linear-gradient(135deg, #f1d2cb 0%, #f7e6e1 55%, #fbf3f0 100%); }
  .post.cream { background: linear-gradient(160deg, #fbf9f6 0%, #efe9e1 60%, #e0d5c8 100%); }

  .photo { position: absolute; }
  .photo.auburn-hair { left: 92px; top: 0; width: 102px; height: 194px; background: linear-gradient(90deg, rgba(183,31,49,0) 0%, #a8452d 35%, #c0653a 60%, #3a2420 100%); }
  .photo.curls-soft { inset: 0; background: radial-gradient(circle at 55% 40%, rgba(120,95,70,0.35), rgba(159,168,150,0) 65%); }
  .photo.salon-floor { left: 0; top: 60px; width: 194px; height: 134px; background: linear-gradient(180deg, rgba(239,203,195,0) 0%, rgba(200,185,178,0.55) 55%, rgba(150,140,140,0.55) 100%); }
  .photo.braid-portrait { left: 0; top: 0; width: 53px; height: 172px; border-radius: 0 0 26px 0; background: linear-gradient(180deg, #a98063 0%, #7b4f38 55%, #6a2232 100%); }

  .tag { position: absolute; height: 13px; line-height: 13px; padding-left: 9px; font: 400 6.3px/13px var(--sans); letter-spacing: 0.3px; text-transform: uppercase; }
  .tag.light { left: 0; width: 86px; background: var(--paper); color: var(--brand-red); border-radius: 0 7px 7px 0; }
  .tag.solid { left: 0; width: 86px; background: var(--brand-red); color: var(--paper); border-radius: 0 7px 7px 0; }
  .tag.solid.floating { left: 61px; border-radius: 7px; }

  .headline { position: absolute; left: 10px; font: 400 14px/16.5px var(--serif); }
  .headline.on-red { color: var(--paper); }
  .headline.on-light { color: var(--brand-red); }
  .headline-rule { position: absolute; left: 10px; width: 10px; height: 1px; }
  .body-copy { position: absolute; left: 10px; width: 72px; font: 400 6.2px/7.8px var(--sans); }
  .body-copy.on-red { color: var(--paper); }
  .body-copy.on-light { color: var(--ink); }

  .quote-line { position: absolute; left: 35px; width: 135px; text-align: center; top: 64px; font: 400 13px/1 var(--script); color: var(--brand-red); }
  .quote-body { position: absolute; left: 42px; width: 120px; text-align: center; top: 79px; font: 400 6.2px/7.8px var(--sans); color: var(--paper); }
  .frame-top { position: absolute; left: 10px; top: 10px; width: 155px; height: 1px; background: rgba(255,255,255,0.75); }
  .frame-side { position: absolute; left: 10px; top: 10px; width: 1px; height: 137px; background: rgba(255,255,255,0.75); }

  .sign-off { position: absolute; right: 10px; top: 150px; font: 400 15px/1 var(--script); color: var(--brand-red); }

  .url-bar { position: absolute; top: 178px; height: 6px; background: var(--paper); font: 400 4.6px/6px var(--sans); letter-spacing: 1px; color: var(--brand-red); white-space: nowrap; }
  .url-bar.left { left: 0; width: 141px; border-radius: 0 3px 3px 0; padding-left: 9px; }
  .url-bar.right { right: 0; width: 141px; border-radius: 3px 0 0 3px; text-align: right; padding-right: 9px; }
  .post.blush .url-bar, .post.cream .url-bar { color: var(--ink); }

  .mini-mark { position: absolute; top: 152px; font-family: var(--serif); font-weight: 400; line-height: 1; }
  .mini-mark .name { display: block; font-size: 19px; }
  .mini-mark .descriptor { display: block; font-size: 3.4px; text-transform: uppercase; letter-spacing: 0.2px; margin-top: 2px; }
  .mini-mark.right { right: 9px; }
  .mini-mark.left { left: 9px; }
  .mini-mark.light { color: var(--paper); }
  .mini-mark.dark { color: var(--ink); }
</style>
</head>
<body>
<main class="board">

  <!-- Brand identity -->
  <h2 class="section-title" style="left:44px; top:25px;">BRAND IDENTITY</h2>
  <div class="section-rule" style="left:44px; top:50px;"></div>
  <div class="wordmark" style="left:44px; top:118px;">
    <span class="name">Tovel</span>
    <span class="descriptor">Hair Design</span>
  </div>

  <!-- Logo variations -->
  <h2 class="section-title" style="left:440px; top:25px;">LOGO VARIATIONS</h2>
  <div class="section-rule" style="left:440px; top:50px;"></div>
  <div class="logo-tile on-ink"><span class="name">Tovel</span><span class="descriptor">Hair Design</span></div>
  <div class="logo-tile on-red"><span class="name">Tovel</span><span class="descriptor">Hair Design</span></div>

  <!-- Color palette -->
  <h2 class="section-title" style="left:44px; top:314px;">COLOR PALETTE</h2>
  <div class="section-rule" style="left:44px; top:337px;"></div>
  <div class="swatch red" style="left:43px; top:351px;"></div>
  <div class="swatch linen" style="left:125px; top:351px;"></div>
  <div class="swatch taupe" style="left:207px; top:351px;"></div>
  <div class="swatch blush" style="left:43px; top:429px;"></div>
  <div class="swatch sage" style="left:125px; top:429px;"></div>
  <div class="swatch ink" style="left:207px; top:429px;"></div>

  <!-- Typography -->
  <h2 class="section-title" style="left:438px; top:314px;">TYPOGRAPHY</h2>
  <div class="section-rule" style="left:438px; top:337px;"></div>

  <div class="specimen-glyph serif">Aa</div>
  <div class="spec-label" style="top:351px;">Headlines</div>
  <div class="spec-name serif-set" style="top:362px; font-size:20px;">Playfair Display</div>
  <div class="spec-weights serif-set" style="top:390px;">Regular / Medium / Bold</div>
  <p class="spec-sample serif-set" style="top:406px;">Lorem ipsum dolor sit amet, consectetuer adipiscing elit, sed diam nonummy nibh euismod tincidunt ut laoreet dolore magna aliquam erat volutpat. Ut wisi enim ad minim veniam, quis nostrud exerci tation ullamcorper suscipit lobortis nisl ut aliquip ex ea commodo consequat. Duis autem vel eum iriure dolor in hendrerit in vulputate velit esse molestie consequat,</p>

  <div class="specimen-glyph sans">Aa</div>
  <div class="spec-label" style="top:468px;">Body Text</div>
  <div class="spec-name sans-set" style="top:478px; font-size:19px; font-weight:400;">Montserrat</div>
  <div class="spec-weights sans-set" style="top:505px;">Regular / Medium / Bold</div>
  <p class="spec-sample sans-set" style="top:522px; font-size:5.6px; line-height:7.4px;">Lorem ipsum dolor sit amet, consectetuer adipiscing elit, sed diam nonummy nibh euismod tincidunt ut laoreet dolore magna aliquam erat volutpat. Ut wisi enim ad minim veniam, quis nostrud exerci tation ullamcorper suscipit lobortis nisl ut aliquip ex ea commodo consequat. Duis autem vel eum iriure dolor in hendrerit in vulputate velit esse molestie consequat,</p>

  <div class="specimen-glyph script">Aa</div>
  <div class="spec-label" style="top:587px;">Accent (Optional)</div>
  <div class="spec-name script-set" style="top:598px; font-size:20px;">Alex Brush</div>
  <div class="spec-weights script-set" style="top:626px; font-size:10px;">Regular</div>
  <p class="spec-sample script-set" style="top:641px; font-size:5.2px;">Lorem ipsum dolor sit amet, consectetuer adipiscing elit, sed diam nonummy nibh euismod tincidunt ut laoreet dolore magna aliquam erat volutpat. Ut wisi enim ad minim veniam, quis nostrud exerci tation ullamcorper suscipit lobortis nisl ut aliquip ex ea commodo consequat. Duis autem vel eum iriure dolor in hendrerit in vulputate velit esse molestie consequat, vel illum dolore eu feugiat nulla facilisis at vero eros et accumsan et iusto odio dignissim.</p>

  <!-- Post templates -->
  <h2 class="section-title" style="left:44px; top:694px;">POST TEMPLATE</h2>
  <div class="section-rule" style="left:44px; top:720px;"></div>

  <!-- Healthy hair tip -->
  <article class="post red" style="left:43px; top:742px;">
    <div class="tag light" style="top:17px;">Healthy Hair Tip</div>
    <h3 class="headline on-red" style="top:44px;">Hydration is<br>the key</h3>
    <div class="headline-rule" style="top:82px; background:var(--paper);"></div>
    <p class="body-copy on-red" style="top:89px;">Well-hydrated hair is stronger, shinier and more resilient.</p>
    <div class="url-bar left">www.tovelhairstudio-example.com</div>
    <div class="mini-mark right light"><span class="name">Tovel</span><span class="descriptor">Hair Design</span></div>
  </article>

  <article class="post red" style="left:243px; top:742px;">
    <div class="photo auburn-hair" role="img" aria-label="Photo of long wavy auburn hair seen from behind"></div>
    <div class="tag light" style="top:17px;">Healthy Hair Tip</div>
    <h3 class="headline on-red" style="top:44px;">Hydration is<br>the key</h3>
    <div class="headline-rule" style="top:82px; background:var(--paper);"></div>
    <p class="body-copy on-red" style="top:89px;">Well-hydrated hair is stronger, shinier and more resilient.</p>
    <div class="url-bar left">www.tovelhairstudio-example.com</div>
    <div class="mini-mark right light"><span class="name">Tovel</span><span class="descriptor">Hair Design</span></div>
  </article>

  <!-- Testimonial -->
  <article class="post sage" style="left:445px; top:742px;">
    <div class="frame-top"></div><div class="frame-side"></div>
    <p class="quote-line">“Tovel is the best!”</p>
    <p class="quote-body">I am so glad I met Elena. I feel we are on a journey together. I trust her vision and skill. Thanks Elena, see you in a couple months --</p>
    <div class="mini-mark left light"><span class="name">Tovel</span><span class="descriptor">Hair Design</span></div>
    <div class="url-bar right">www.tovelhairstudio-example.com</div>
  </article>

  <article class="post sage" style="left:648px; top:742px;">
    <div class="photo curls-soft" role="img" aria-label="Faded photo of soft brown curls"></div>
    <div class="frame-top"></div><div class="frame-side"></div>
    <p class="quote-line">“Tovel is the best!”</p>
    <p class="quote-body">I am so glad I met Elena. I feel we are on a journey together. I trust her vision and skill. Thanks Elena, see you in a couple months --</p>
    <div class="mini-mark left light"><span class="name">Tovel</span><span class="descriptor">Hair Design</span></div>
    <div class="url-bar right">www.tovelhairstudio-example.com</div>
  </article>

  <!-- Reminder -->
  <article class="post blush" style="left:43px; top:944px;">
    <div class="tag solid" style="top:24px;">Reminder</div>
    <h3 class="headline on-light" style="top:60px;">Holyday Hours</h3>
    <div class="headline-rule" style="top:80px; background:var(--brand-red);"></div>
    <p class="body-copy on-light" style="top:79px; margin-top:6px;">We will be closed Monday, May 26 for Memorial Day.</p>
    <p class="sign-off">Thank you!</p>
    <div class="mini-mark left dark"><span class="name">Tovel</span><span class="descriptor">Hair Design</span></div>
    <div class="url-bar right" style="width:142px;">www.tovelhairstudio-example.com</div>
  </article>

  <article class="post blush" style="left:243px; top:944px;">
    <div class="photo salon-floor" role="img" aria-label="Soft-focus photo of the salon interior with styling chairs"></div>
    <div class="tag solid" style="top:24px;">Reminder</div>
    <h3 class="headline on-light" style="top:60px;">Holyday Hours</h3>
    <div class="headline-rule" style="top:80px; background:var(--brand-red);"></div>
    <p class="body-copy on-light" style="top:79px; margin-top:6px;">We will be closed Monday, May 26 for Memorial Day.</p>
    <p class="sign-off">Thank you!</p>
    <div class="mini-mark left dark"><span class="name">Tovel</span><span class="descriptor">Hair Design</span></div>
    <div class="url-bar right" style="width:142px;">www.tovelhairstudio-example.com</div>
  </article>

  <!-- Service spotlight -->
  <article class="post cream" style="left:445px; top:944px;">
    <div class="tag solid" style="top:24px;">Service Spotlight</div>
    <h3 class="headline on-light" style="top:60px;">Grey Blending</h3>
    <div class="headline-rule" style="top:80px; background:var(--brand-red);"></div>
    <p class="body-copy on-light" style="top:85px; width:90px;">Seamless, natural results designed just for you.</p>
    <div class="url-bar left" style="width:146px;">www.tovelhairstudio-example.com</div>
    <div class="mini-mark right dark"><span class="name">Tovel</span><span class="descriptor">Hair Design</span></div>
  </article>

  <article class="post cream" style="left:648px; top:944px;">
    <div class="photo braid-portrait" role="img" aria-label="Photo of long braided curly hair seen from behind"></div>
    <div class="tag solid floating" style="top:24px;">Service Spotlight</div>
    <h3 class="headline on-light" style="top:60px; left:72px;">Grey Blending</h3>
    <div class="headline-rule" style="top:80px; left:72px; background:var(--brand-red);"></div>
    <p class="body-copy on-light" style="top:85px; left:72px; width:90px;">Seamless, natural results designed just for you.</p>
    <div class="url-bar left">www.tovelhairstudio-example.com</div>
    <div class="mini-mark right dark"><span class="name">Tovel</span><span class="descriptor">Hair Design</span></div>
  </article>

</main>
</body>
</html>
```